Premium modern eliquids labels 84.5 x 80 mm

I am looking for modern graphics for the labels of a new eliquid line that will have 4 different types of eliquids. It will have a tobacco one (brown colours maybe), a fruity one (bright colours maybe), a minty one (green colours maybe) and a creamy one (beige colours maybe).
I will need one of them to see how the design is, that design will have to be adapted to the other 3 colours of the label.
The brand logo is attached. I also attached a sample of what is mandatory to write on the label, you can change size, place and font of what is written, the only thing that cannot be reduced is the yellow parts. I attach the bottle that we will use.The size of the label is 84.5 x 80 mm (base x height).

Target Market(s)

vapers

Requirements
Must have
• My project must have one of the labels.

```html
<!DOCTYPE html>
<html lang="it">
<head>
<meta charset="utf-8">
<title>Velora Vapes – Fruzz label</title>
<link rel="stylesheet" href="https://fonts.googleapis.com/css2?family=Chewy&family=Montserrat:wght@500;600;700;800;900&display=swap">
<style>
  :root{
    --stage:#207dbb;
    --paper:#ffffff;
    --ink:#111111;
    --pale-yellow:#fafa9a;
    --brand-blue:#6bbde6;
    --name-red:#fb0000;
    --name-yellow:#fff27a;
    --tag-yellow:#fdc332;
    --fruit-orange:#ff6b08;
    --fruit-lemon:#ffe300;
    --fruit-strawberry:#f2264a;
    --fruit-pineapple:#fdbb10;
    --fruit-apple:#fb2b1f;
  }
  *{box-sizing:border-box;margin:0;padding:0}
  html,body{width:1200px;height:1200px;overflow:hidden}
  body{background:var(--stage);font-family:"Montserrat",sans-serif;color:var(--ink);position:relative}

  .label{position:absolute;left:201px;top:208px;width:828px;height:784px;background:var(--paper);overflow:hidden}

  /* left info panel */
  .ingredients{position:absolute;left:24px;top:23px;font-size:15px;font-weight:700;line-height:18.3px;text-transform:uppercase}
  .lot{position:absolute;left:22px;top:601px;transform-origin:0 0;transform:rotate(-90deg);white-space:nowrap;font-size:15.5px;font-weight:700;line-height:16px;letter-spacing:.2px}
  .packer{position:absolute;left:24px;top:659px}
  .packer-name{font-size:15.5px;font-weight:500;line-height:18.5px;white-space:nowrap}
  .packer-details{margin-top:3px;font-size:11.8px;font-weight:700;line-height:12px;white-space:nowrap}

  /* centre artwork panel */
  .artwork{position:absolute;left:182px;top:0;width:465px;height:784px;background:var(--pale-yellow);overflow:hidden}
  .fruit{position:absolute;border-radius:50%}
  .fruit.orange{background:var(--fruit-orange)}
  .fruit.lemon{background:var(--fruit-lemon)}
  .fruit.strawberry{background:var(--fruit-strawberry)}
  .fruit.pineapple{background:var(--fruit-pineapple)}
  .fruit.apple{background:var(--fruit-apple)}

  .orange-top{left:-14px;top:-40px;width:110px;height:100px}
  .lemon-top{left:167px;top:-18px;width:120px;height:94px}
  .strawberry-top-left{left:76px;top:58px;width:93px;height:83px}
  .strawberry-top-right{left:322px;top:50px;width:92px;height:83px}
  .pineapple-top{left:388px;top:-30px;width:100px;height:70px}
  .orange-mid{left:-20px;top:345px;width:114px;height:116px}
  .lemon-mid{left:170px;top:366px;width:116px;height:110px}
  .strawberry-mid{left:325px;top:410px;width:70px;height:81px}
  .pineapple-mid{left:380px;top:335px;width:110px;height:107px}
  .pineapple-bottom{left:-10px;top:673px;width:120px;height:110px}
  .apple-bottom{left:164px;top:715px;width:96px;height:100px}
  .orange-bottom{left:392px;top:699px;width:100px;height:110px}

  .brand{position:absolute;left:21px;top:190px;width:428px;height:110px;display:flex;align-items:center;justify-content:center;gap:10px;font-weight:900;font-size:46px;letter-spacing:.5px;color:var(--brand-blue);text-transform:uppercase;white-space:nowrap}
  .brand-dot{width:16px;height:16px;border-radius:50%;background:var(--brand-blue)}

  .flavour-name{position:absolute;left:74px;top:523px;width:322px;height:155px;border-radius:44px;background:var(--name-red);display:flex;align-items:center;justify-content:center;font-family:"Chewy",sans-serif;font-weight:400;font-size:92px;letter-spacing:3px;color:var(--name-yellow);text-transform:uppercase;padding-top:6px}

  /* right info panel */
  .instructions{position:absolute;left:675px;top:24px;white-space:nowrap}
  .instructions h2{font-size:20.5px;font-weight:700;line-height:18.5px;text-transform:uppercase}
  .instructions p{margin-top:19px;font-size:16.5px;font-weight:500;line-height:19.3px}

  .tag{position:absolute;background:var(--tag-yellow);font-weight:800;text-transform:uppercase;display:flex;align-items:center;justify-content:center;color:#111}
  .tag-collection{left:676px;width:118px;height:37px;font-size:17px;line-height:16px;text-align:center;flex-direction:column}
  .tag-code{left:676px;width:85px;height:37px;font-size:21px;letter-spacing:.5px}
  .tag-part{position:absolute;left:676px;font-size:9.5px;font-weight:700;text-transform:uppercase}
  .collection-label{top:343px}
  .part-label{top:386px}
  .code-label{top:404px}
  .collection-bottle{top:461px}
  .part-bottle{top:505px}
  .code-bottle{top:521px}

  .icon-recycle{position:absolute;left:690px;top:654px}
  .icon-bin{position:absolute;left:750px;top:638px}
  .volume{position:absolute;left:680px;top:729px;width:118px;text-align:center;font-size:16px;font-weight:800;white-space:nowrap}
</style>
</head>
<body>
<main class="label">
  <section class="info-left">
    <p class="ingredients">Ingredienti:<br>Glicole<br>propilenico<br>sostanze<br>aromatizzanti</p>
    <p class="lot">L.SH20 - 001-PES-D.PROD.22-04-2022 D.SC.21-04-2024</p>
    <div class="packer">
      <p class="packer-name">E CONFEZIONATO<br>DA Nordvia srl</p>
      <p class="packer-details">10100 Torino<br>P.i.00000000000<br>Tel. +39 000 0000000<br>info@nordvia.it</p>
    </div>
  </section>

  <section class="artwork">
    <div class="fruit orange orange-top" role="img" aria-label="Cartoon orange illustration"></div>
    <div class="fruit lemon lemon-top" role="img" aria-label="Cartoon lemon illustration"></div>
    <div class="fruit strawberry strawberry-top-left" role="img" aria-label="Cartoon strawberry illustration"></div>
    <div class="fruit strawberry strawberry-top-right" role="img" aria-label="Cartoon strawberry illustration"></div>
    <div class="fruit pineapple pineapple-top" role="img" aria-label="Cartoon pineapple illustration"></div>
    <div class="fruit orange orange-mid" role="img" aria-label="Cartoon orange illustration"></div>
    <div class="fruit lemon lemon-mid" role="img" aria-label="Cartoon lemon illustration"></div>
    <div class="fruit strawberry strawberry-mid" role="img" aria-label="Cartoon strawberry illustration"></div>
    <div class="fruit pineapple pineapple-mid" role="img" aria-label="Cartoon pineapple illustration"></div>
    <div class="fruit pineapple pineapple-bottom" role="img" aria-label="Cartoon pineapple illustration"></div>
    <div class="fruit apple apple-bottom" role="img" aria-label="Cartoon apple illustration"></div>
    <div class="fruit orange orange-bottom" role="img" aria-label="Cartoon orange illustration"></div>

    <div class="brand"><span class="brand-dot"></span>Velora Vapes</div>
    <h1 class="flavour-name">Fruzz</h1>
  </section>

  <section class="info-right">
    <div class="instructions">
      <h2>Istruzioni<br>d’uso:</h2>
      <p>Agitare bene<br>prima<br>dell’utilizzo.<br>Diluire nelle<br>percentuali<br>consigliate<br>sul nostro<br>sito.<br>Conservare in<br>luogo fresco e<br>asciutto</p>
    </div>

    <div class="tag tag-collection collection-label"><span>Raccolta</span><span>plastica</span></div>
    <p class="tag-part part-label">Etichetta</p>
    <div class="tag tag-code code-label">PAP 5</div>

    <div class="tag tag-collection collection-bottle"><span>Raccolta</span><span>plastica</span></div>
    <p class="tag-part part-bottle">Flacone</p>
    <div class="tag tag-code code-bottle">PET 1</div>

    <svg class="icon-recycle" width="50" height="50" viewBox="0 0 50 50" fill="none" stroke="#111" stroke-width="2" stroke-linejoin="round">
      <path d="M19 6 L31 6 L37 16 L41 14 L39 25 L29 22 L33 20 L28 12 L22 12 L17 20 L12 17 Z"/>
      <path d="M10 22 L4 32 L10 43 L21 43 L21 48 L29 40 L21 33 L21 37 L14 37 L10 31 L15 25 Z"/>
      <path d="M40 24 L46 34 L40 44 L30 44 L30 38 L36 38 L40 32 L36 27 Z"/>
    </svg>
    <svg class="icon-bin" width="48" height="66" viewBox="0 0 48 66" fill="#111">
      <circle cx="34" cy="6" r="5.5"/>
      <path d="M28 14 L42 14 L44 40 L40 40 L40 65 L36 65 L36 42 L34 42 L34 65 L30 65 L30 30 L18 36 L16 33 L28 24 Z"/>
      <circle cx="9" cy="30" r="1.4"/><circle cx="12" cy="34" r="1.4"/><circle cx="8" cy="36" r="1.4"/>
      <path d="M1 40 L21 40 L18 64 L4 64 Z" fill="none" stroke="#111" stroke-width="2.5"/>
    </svg>
    <p class="volume">20 ML NET</p>
  </section>
</main>
</body>
</html>
```